Design the Keystone HR business card for my new business

I've just had a logo designed (attached) for my new business doing HR consulting. I'm a one person operation at this stage, my aim is to provide support and help to small to medium sized businesses with their people objectives or issues.

I'm not really into anything overly flashy, I'm not a PR or marketing agency. I'd like my card to look modern, professional and not gimmicky.

I'm thinking black front (to go with logo), double sided with details on the back, maybe in a different colour?

Logo attached in several different formats.

Front of the card to have logo and added text: People and Development Solutions

Back of the card to also feature logo in some way and say:
Megan Tulloch
PO Box (TBA)
Marrowvale QLD 4391
0438 512 976
megan@keystonehr.com.au
www.keystonehr.com.au

Target Market(s)

Small to medium businesses / business owners.

Industry/Entity Type

Marketing

Requirements
Must have
• Double sided business card.
Should not have
• Anything overly gimmicky.

```html
<!DOCTYPE html>
<html lang="en">
<head>
<meta charset="utf-8">
<title>Keystone HR – Business Card</title>
<link href="https://fonts.googleapis.com/css2?family=Questrial&family=Arimo:wght@400&display=swap" rel="stylesheet">
<style>
  :root {
    --backdrop: #737373;
    --card-black: #000000;
    --accent-purple: #5b3a78;
    --ring-purple: #7a4fa3;
    --photo-light: #e6e7f1;
    --photo-mid: #c9cade;
    --photo-deep: #aeb0cc;
    --text-white: #ffffff;
    --text-dark: #111111;
  }
  * { margin: 0; padding: 0; box-sizing: border-box; }
  html, body { width: 1200px; height: 1104px; overflow: hidden; }
  body { background: var(--backdrop); position: relative; }

  .card {
    position: absolute;
    left: 262px;
    width: 662px;
    height: 496px;
    overflow: hidden;
  }
  .card--front { top: 55px; }
  .card--back  { top: 564px; }

  .card__art { position: absolute; inset: 0; width: 100%; height: 100%; }

  .brand-ring {
    position: absolute;
    width: 118px; height: 118px;
    border: 2px solid var(--ring-purple);
    border-radius: 50%;
  }
  .brand-name {
    position: absolute;
    font-family: "Questrial", sans-serif;
    font-weight: 400;
    font-size: 30px;
    line-height: 1;
    color: var(--text-white);
    white-space: nowrap;
    letter-spacing: -0.3px;
  }
  .tagline {
    position: absolute;
    font-family: "Arimo", sans-serif;
    font-size: 8px;
    letter-spacing: 0.1px;
    color: var(--text-white);
    white-space: nowrap;
  }

  .card--front .brand-ring { left: 45px; top: 292px; }
  .card--front .brand-name { left: 190px; top: 334px; }
  .card--front .tagline    { left: 191px; top: 401px; }

  .card--back .brand-ring { left: 343px; top: 291px; }
  .card--back .brand-name { left: 484px; top: 334px; }
  .card--back .tagline    { left: 486px; top: 405px; }

  .contact {
    position: absolute;
    left: 25px;
    top: 178px;
    font-family: "Arimo", sans-serif;
    font-size: 17.5px;
    line-height: 23.8px;
    color: var(--text-dark);
    list-style: none;
  }
</style>
</head>
<body>

<section class="card card--front" aria-label="Card front">
  <svg class="card__art" viewBox="0 0 600 450" preserveAspectRatio="none">
    <defs>
      <linearGradient id="interiorFront" x1="0" y1="0" x2="0" y2="1">
        <stop offset="0" stop-color="var(--photo-light)"/>
        <stop offset="0.6" stop-color="var(--photo-mid)"/>
        <stop offset="1" stop-color="var(--photo-deep)"/>
      </linearGradient>
    </defs>
    <rect width="600" height="450" fill="url(#interiorFront)" role="img" aria-label="Photo of a bright modern office interior"/>
    <path d="M100 48 L222 0 L238 0 Z" fill="var(--accent-purple)"/>
    <path d="M340 200 L415 340 Q418 358 402 372 L225 450 L250 450 Z" fill="var(--accent-purple)"/>
    <path d="M0 0 L270 0 L398 340 Q405 362 385 375 L218 450 L0 450 Z" fill="var(--card-black)"/>
  </svg>
  <span class="brand-ring" aria-hidden="true"></span>
  <span class="brand-name">Keystone HR</span>
  <span class="tagline">PEOPLE AND DEVELOPMENT SOLUTIONS</span>
</section>

<section class="card card--back" aria-label="Card back">
  <svg class="card__art" viewBox="0 0 600 450" preserveAspectRatio="none">
    <defs>
      <linearGradient id="interiorBack" x1="0" y1="0" x2="0" y2="1">
        <stop offset="0" stop-color="var(--photo-light)"/>
        <stop offset="0.6" stop-color="var(--photo-mid)"/>
        <stop offset="1" stop-color="var(--photo-deep)"/>
      </linearGradient>
    </defs>
    <rect width="600" height="450" fill="url(#interiorBack)" role="img" aria-label="Photo of a bright modern office interior"/>
    <g transform="translate(600 0) scale(-1 1)">
      <path d="M20 0 L122 50 L142 50 Z" fill="var(--accent-purple)"/>
      <path d="M265 160 L335 320 Q338 340 322 350 L140 450 L165 450 Z" fill="var(--accent-purple)"/>
      <path d="M0 0 L188 0 L318 315 Q325 338 305 350 L160 450 L0 450 Z" fill="var(--card-black)"/>
    </g>
  </svg>
  <ul class="contact">
    <li>Megan Tulloch</li>
    <li>PO Box (TBA)</li>
    <li>Marrowvale QLD 4391</li>
    <li>0438 512 976</li>
    <li>megan@keystonehr.com.au</li>
    <li>www.keystonehr.com.au</li>
  </ul>
  <span class="brand-ring" aria-hidden="true"></span>
  <span class="brand-name">Keystone HR</span>
  <span class="tagline">PEOPLE AND DEVELOPMENT SOLUTIONS</span>
</section>

</body>
</html>
```